DRIFTFRAME studio

Design to be modern with colours of logo, maybe orange background. Include name, position, phone/WhatsApp email/web. Specialises in long form TIMELAPSE

Contact Information for Business Card

Marcel Okoro, filmmaker,/photographer, phone/WhatsApp +971529386047, email - marcel@driftframestudio.com www.driftframestudio.com, instagram @driftframestudio

Font styles to use
Sans Serif

Requirements
Must have
• Fresh, bright, modern, original
Marcel Okoro - Filmmaker/Photographer
Phone/WhatsApp +971 529 38 6047
email - marcel@driftfarmestudio.com
Web - driftfarmestudio.com
PoBox 584319, Dubai, UAE
instagram - driftframestudio
Should not have
• solid black background

```html
<!DOCTYPE html>
<html lang="en">
<head>
<meta charset="utf-8">
<title>DRIFTFRAME studio – Business Card</title>
<link rel="stylesheet" href="https://fonts.googleapis.com/css2?family=Roboto:wght@400;500;700&display=swap">
<style>
  :root {
    --backdrop: #545454;
    --card: #2e2e2e;
    --orange: #e3701f;
    --light: #d9d9d9;
    --shadow: rgba(0, 0, 0, 0.45);
  }
  * { margin: 0; padding: 0; box-sizing: border-box; }
  html, body {
    width: 1200px;
    height: 900px;
    overflow: hidden;
    background: var(--backdrop);
    font-family: "Roboto", Arial, sans-serif;
  }
  .stage {
    position: relative;
    width: 1200px;
    height: 900px;
  }
  .card {
    position: absolute;
    left: 290px;
    width: 620px;
    height: 354px;
    background: var(--card);
    box-shadow: 0 14px 30px var(--shadow);
  }
  .card--back { top: 56px; }
  .card--front { top: 470px; }

  /* Back side */
  .brand-lockup {
    position: absolute;
    left: 0;
    right: 0;
    top: 128px;
    display: flex;
    justify-content: center;
    align-items: center;
    gap: 16px;
  }
  .brand-dot {
    width: 34px;
    height: 34px;
    border-radius: 50%;
    border: 4px solid var(--orange);
  }
  .brand-name {
    font-weight: 700;
    font-size: 44px;
    letter-spacing: 1px;
    color: var(--orange);
  }
  .back-web {
    position: absolute;
    left: 0;
    right: 0;
    top: 230px;
    text-align: center;
    font-size: 15px;
    color: var(--light);
    letter-spacing: 0.5px;
  }

  /* Front side */
  .front-brand {
    position: absolute;
    left: 48px;
    top: 38px;
    display: flex;
    align-items: center;
    gap: 9px;
  }
  .front-brand .brand-dot {
    width: 18px;
    height: 18px;
    border-width: 2.5px;
  }
  .front-brand .brand-name {
    font-size: 21px;
  }
  .person-name {
    position: absolute;
    left: 48px;
    top: 104px;
    font-size: 27px;
    font-weight: 500;
    color: var(--orange);
  }
  .person-role {
    position: absolute;
    left: 48px;
    top: 140px;
    font-size: 14px;
    color: var(--light);
  }
  .accent-rule {
    position: absolute;
    left: 222px;
    right: 0;
    top: 150px;
    height: 1.5px;
    background: var(--orange);
  }
  .contact-list {
    position: absolute;
    left: 48px;
    top: 176px;
    list-style: none;
  }
  .contact-item {
    display: flex;
    align-items: center;
    gap: 12px;
    height: 24px;
    font-size: 14px;
    color: var(--light);
  }
  .contact-icon {
    width: 14px;
    height: 14px;
    flex: none;
  }
  .address {
    position: absolute;
    right: 40px;
    bottom: 30px;
    font-size: 14px;
    color: var(--light);
    letter-spacing: 0.3px;
  }
</style>
</head>
<body>
<main class="stage">

  <section class="card card--back" aria-label="Card back">
    <div class="brand-lockup">
      <span class="brand-dot"></span>
      <span class="brand-name">DRIFTFRAME studio</span>
    </div>
    <p class="back-web">driftfarmestudio.com</p>
  </section>

  <section class="card card--front" aria-label="Card front">
    <div class="front-brand">
      <span class="brand-dot"></span>
      <span class="brand-name">DRIFTFRAME studio</span>
    </div>

    <h1 class="person-name">Marcel Okoro</h1>
    <p class="person-role">Filmmaker/Photographer</p>
    <div class="accent-rule"></div>

    <ul class="contact-list">
      <li class="contact-item">
        <svg class="contact-icon" viewBox="0 0 24 24" aria-hidden="true">
          <path fill="#e3701f" d="M6.6 10.8a15.1 15.1 0 0 0 6.6 6.6l2.2-2.2a1 1 0 0 1 1-.25 11.4 11.4 0 0 0 3.6.57 1 1 0 0 1 1 1V20a1 1 0 0 1-1 1A17 17 0 0 1 3 4a1 1 0 0 1 1-1h3.5a1 1 0 0 1 1 1c0 1.25.2 2.45.57 3.57a1 1 0 0 1-.25 1z"/>
        </svg>
        +971 529 38 6047
      </li>
      <li class="contact-item">
        <svg class="contact-icon" viewBox="0 0 24 24" aria-hidden="true">
          <rect x="2" y="5" width="20" height="14" rx="1.5" fill="#e3701f"/>
          <path d="M3 6.5l9 6.5 9-6.5" fill="none" stroke="#2e2e2e" stroke-width="2"/>
        </svg>
        marcel@driftfarmestudio.com
      </li>
      <li class="contact-item">
        <svg class="contact-icon" viewBox="0 0 24 24" aria-hidden="true">
          <circle cx="12" cy="12" r="9" fill="#e3701f"/>
        </svg>
        driftframestudio
      </li>
      <li class="contact-item">
        <svg class="contact-icon" viewBox="0 0 24 24" aria-hidden="true">
          <g fill="none" stroke="#e3701f" stroke-width="2">
            <circle cx="12" cy="12" r="9.5"/>
            <ellipse cx="12" cy="12" rx="4.2" ry="9.5"/>
            <path d="M2.5 12h19M4 7h16M4 17h16"/>
          </g>
        </svg>
        driftfarmestudio.com
      </li>
    </ul>

    <p class="address">PoBox 584319, Dubai, UAE</p>
  </section>

</main>
</body>
</html>
```